Web site for mobile& web developers

We need a web site design for our company, Marlow Fenwick Studio Pty Ltd.

We are a Sydney based, software development company specialising in mobile platforms and web applications. We are a small, dynamic team with a few awesome products we want to get out to the world.

We would prefer a clean, professional layout that incorporates the company logo and branding; we do have a youthful, start-up edge which we would like to express.

We technical people with damn good products, so your design has to make us look good to non-technical people too!

Target Market(s)

B2B, Enterprise technology, Project Managers, Marketing, Other developers

Industry/Entity Type

It Company

Requirements
Must have
• Required pages:
- home page - this must allow us to feature our software (mobile & web) on the home page
- a standard content page (for things like "about us", "our team", etc)
- contact us (including HTML form with error state)
- mobile (iOS and Android) product page - allow for screen shots, features, requirements, customer list
- web product page - allow for screen shots, features, requirements, customer list

You must incorporate our logo and branding into the theme.
Should not have
• HTML/CSS carve is not required. We only required layered PNGs or PSDs.

```html
<!DOCTYPE html>
<html lang="en">
<head>
<meta charset="utf-8">
<title>Marlow Fenwick Studio</title>
<link href="https://fonts.googleapis.com/css2?family=Source+Sans+3:ital,wght@0,400;0,600;0,700;1,400&display=swap" rel="stylesheet">
<style>
:root{
  --blue:#1a73c4;
  --blue-dark:#0b5aa6;
  --teal:#2f6a80;
  --red:#e8452a;
  --green:#3aa93a;
  --orange:#f39a1e;
  --ink:#222;
  --muted:#555;
  --hero-bg:#eeeeee;
  --band:#e3e3e3;
  --footer:#4b4b4b;
  --footer-text:#e4e4e4;
  --accent-light:#8db3de;
}
*{box-sizing:border-box;margin:0;padding:0}
html,body{width:1200px;height:1012px;overflow:hidden}
body{font-family:"Source Sans 3",sans-serif;color:var(--ink);background:#fff;position:relative}
.abs{position:absolute}
.top-stripe{left:0;top:0;width:1200px;height:4px;background:repeating-linear-gradient(90deg,var(--blue) 0 6px,#7fb6e6 6px 9px,#2d85d0 9px 14px)}
.site-header{left:0;top:4px;width:1200px;height:106px;background:#f7f7f7}
.brand{left:204px;top:48px;display:flex;align-items:center;gap:12px;font-size:24px;letter-spacing:4px;color:#777;font-weight:600}
.brand-dot{width:52px;height:52px;border-radius:50%;background:var(--blue)}
.contact-info{left:851px;top:18px;font-size:13px;line-height:16px;color:var(--blue);font-weight:600}
.contact-info div{display:flex;align-items:center;gap:6px}
.main-nav{left:704px;top:72px;width:295px;height:28px;border:1px solid var(--blue);display:flex;align-items:center;font-size:11.5px;background:#fff}
.main-nav a{color:var(--ink);text-decoration:none;padding:0 8px;height:100%;display:flex;align-items:center}
.main-nav a.active{background:var(--blue);color:#fff;font-weight:600;padding:0 11px}
.hero{left:0;top:110px;width:1200px;height:301px;background:var(--hero-bg)}
.hero-line{font-weight:600;position:absolute;white-space:nowrap}
.hero .l1{left:204px;top:48px;font-size:25px;color:var(--teal)}
.hero .l2{left:255px;top:81px;font-size:46px;color:var(--red)}
.hero .l3{left:204px;top:137px;font-size:25px;color:var(--teal)}
.hero .l3 span{color:var(--green)}
.hero .l4{left:288px;top:168px;font-size:25px;color:var(--orange)}
.quote-btn{position:absolute;left:226px;top:230px;width:180px;height:33px;background:linear-gradient(#4d9ae6,var(--blue-dark));display:flex;color:#fff;font-weight:600;font-size:20px}
.quote-btn .label{flex:1;display:flex;align-items:center;justify-content:center}
.quote-btn .arrow{width:23px;border-left:1px solid rgba(255,255,255,.5);display:flex;align-items:center;justify-content:center}
.hero-devices{position:absolute;left:475px;top:29px;width:570px;height:261px;background:linear-gradient(180deg,#555 0%,#2f2f2f 80%,#cfcfcf 100%);border-radius:8px}
.slider-bar{left:0;top:411px;width:1200px;height:32px;background:#eaeaea;border-top:1px solid #ddd;border-bottom:1px solid #ddd}
.dot{position:absolute;top:12px;width:9px;height:9px;border-radius:50%}
.welcome{left:196px;top:468px;width:540px}
.welcome h1{font-size:19px;font-weight:600;color:var(--teal);display:flex;align-items:center;gap:6px}
.welcome h1 b{color:#444;font-weight:600}
.welcome h1 .sky{color:#777;font-weight:400}
.welcome h1 i{width:22px;height:22px;border-radius:50%;background:var(--blue);display:inline-block}
.welcome p{font-size:11px;line-height:14px;margin-top:13px}
.welcome h1+p{margin-top:4px}
.work{left:805px;top:472px;width:195px}
.work h2{font-size:16.5px;font-weight:600;margin-bottom:10px}
.work-item{font-size:11px;border-bottom:1px solid var(--accent-light);padding:7px 4px;display:flex;gap:4px}
.work-item.open{background:var(--accent-light);border:none}
.work-panel{display:flex;padding:6px 4px;border-bottom:1px solid var(--accent-light);font-size:9.5px;line-height:12px;background:#f6f6f6}
.work-panel .txt{flex:1}
.work-panel .more{font-weight:600;margin-top:6px}
.work-panel .phone-shot{width:42px;height:56px;background:linear-gradient(#3d6fa8,#1b2e4a);border-radius:6px;margin-left:6px}
.partners{left:0;top:693px;width:1200px;height:78px;background:var(--band);display:flex;align-items:center;justify-content:center;gap:34px;font-weight:700;font-size:21px;color:#1c1c1c}
.partners span{display:flex;align-items:center;gap:6px}
.partners em{font-style:normal;width:14px;height:14px;background:#1d2f5e;display:inline-block}
.site-footer{left:0;top:771px;width:1200px;height:162px;background:var(--footer);border-top:4px dashed #666;color:var(--footer-text)}
.col{position:absolute;top:14px}
.col h3{font-size:13px;font-weight:600;color:#fff;margin-bottom:10px}
.testimonial{left:197px;width:215px;font-size:11px;line-height:14px}
.testimonial q{font-style:italic;display:block}
.testimonial .who{margin-top:12px;font-weight:600;line-height:14px;color:#fff}
.view-all{position:absolute;font-size:11px;font-weight:600;color:#fff}
.divider{position:absolute;top:14px;height:135px;border-left:1px dashed #777}
.connect{left:540px;width:200px}
.social{display:grid;grid-template-columns:repeat(4,21px);gap:5px 8px;margin-left:13px}
.social i{width:21px;height:21px;border-radius:3px;display:block}
.newsletter{margin-top:18px}
.email-field{margin-top:6px;width:138px;height:22px;background:#fff;border-radius:11px;display:flex;align-items:center;justify-content:space-between;padding-left:9px;font-size:9.5px;font-weight:600;color:#333}
.email-field b{width:22px;height:22px;border-radius:50%;background:#5e9bd6;color:#fff;font-size:9px;display:flex;align-items:center;justify-content:center}
.tweets{left:808px;width:182px}
.tweets h3{display:flex;align-items:center;gap:6px}
.tweets h3 i{width:18px;height:18px;background:#333;border-radius:3px;display:inline-block}
.tweet{font-size:9.5px;line-height:12px;padding:2px 0 6px;border-bottom:1px dashed #777;margin-bottom:5px}
.bottom-bar{left:0;top:933px;width:1200px;height:79px;background:#f7f7f7;border-top:1px solid #333}
.bottom-bar::after{content:"";position:absolute;left:0;bottom:0;width:1200px;height:12px;background:repeating-linear-gradient(90deg,#ddd 0 4px,#eee 4px 8px)}
.copyright{position:absolute;left:196px;top:29px;font-size:11.5px;color:#444;font-weight:600}
.footer-nav{position:absolute;right:201px;top:29px;font-size:11.5px;color:#444;font-weight:600}
</style>
</head>
<body>
<div class="abs top-stripe"></div>

<header class="abs site-header">
  <div class="abs brand" style="top:44px">MARLOW FENWICK <span class="brand-dot"></span></div>
  <div class="abs contact-info">
    <div><svg width="11" height="9" viewBox="0 0 11 9"><path d="M1 3 Q5.5 -1 10 3 L8 4 L7 2.5 H4 L3 4Z M2 5 H9 V8 H2Z" fill="#8aaed6"/></svg>+61 2 9000 4518</div>
    <div><svg width="11" height="11" viewBox="0 0 11 11"><circle cx="5.5" cy="5.5" r="4.5" fill="none" stroke="#8aaed6"/><path d="M1 5.5H10M5.5 1V10" stroke="#8aaed6"/></svg>hello@marlowfenwick.example</div>
  </div>
  <nav class="abs main-nav">
    <a class="active" href="#">Home</a><a href="#">About Us</a><a href="#">News</a><a href="#">Products</a><a href="#">Contact Us</a>
  </nav>
</header>

<section class="abs hero">
  <div class="hero-line l1">Flexible</div>
  <div class="hero-line l2">Solutions</div>
  <div class="hero-line l3">For <span>Digital Product</span></div>
  <div class="hero-line l4">Development</div>
  <div class="quote-btn"><span class="label">GET A QUOTE</span><span class="arrow"><svg width="8" height="10"><path d="M0 0L8 5L0 10Z" fill="#fff"/></svg></span></div>
  <div class="hero-devices" role="img" aria-label="Phone, tablet and laptop showing the studio's brand screen"></div>
</section>

<div class="abs slider-bar">
  <span class="dot" style="left:584px;background:#1a8ad8"></span>
  <span class="dot" style="left:600px;background:#bbb"></span>
</div>

<section class="abs welcome">
  <h1>WELCOME TO <b>MARLOW</b><span class="sky">FENWICK</span><i></i></h1>
  <p>We are passionate about quality products. Our core focus is on producing quality user centric products from your ideas. Bleeding edge technologies, high-volume consumer digital products and knowing your audience are our bread and butter.</p>
  <p>We are the leading online and mobile technology BPO in the Asia Pacific region. We have the passion, the talent and the network to make your idea the next big thing.</p>
  <p>Lorem Ipsum is simply dummy text of the printing and typesetting industry. Lorem Ipsum has been the industry's standard dummy text ever since the 1500s, when an unknown printer took a galley of type and scrambled it to make a type specimen book. It has survived not only five centuries, but also the leap into electronic typesetting, remaining essentially unchanged.</p>
</section>

<aside class="abs work">
  <h2>WORK WITH US:</h2>
  <div class="work-item open">→ MOBILE</div>
  <div class="work-panel">
    <div class="txt">Lorem Ipsum is simply dummy text of the printing and type-setting industry.<div class="more">+ Read More</div></div>
    <div class="phone-shot" role="img" aria-label="Smartphone product shot"></div>
  </div>
  <div class="work-item">→ PYTHON</div>
  <div class="work-item" style="border:none">→ DIGITAL EXPERIENCE</div>
</aside>

<section class="abs partners">
  <span><em></em>Norvane</span>
  <span>Quillbright</span>
  <span>HALVORSEN</span>
  <span style="font-size:15px"><em></em>Open Screen Guild</span>
  <span><em></em>Norvane</span>
  <span>Quillbright</span>
</section>

<footer class="abs site-footer">
  <div class="col testimonial">
    <h3>What our Client Says About Us...</h3>
    <q>Lorem Ipsum is simply dummy text of the printing and typesetting industry. Lorem Ipsum has been the industry's standard dummy text ever since the including versions of Lorem Ipsum.</q>
    <div class="who">Warren Ashby<br>C.E.O. Quillbright</div>
  </div>
  <span class="view-all" style="left:357px;top:137px">+ View All</span>
  <span class="divider" style="left:476px"></span>
  <div class="col connect">
    <h3 style="margin-left:13px">Connect Us...</h3>
    <div class="social">
      <i style="background:#3b5c9a"></i><i style="background:#e8762a"></i><i style="background:#3fb3e0"></i><i style="background:#1f7bb6"></i>
      <i style="background:#e9e9e9"></i><i style="background:#6a9a2e"></i><i style="background:#c9302c"></i><i style="background:#f2f2f2"></i>
    </div>
    <div class="newsletter"><h3 style="margin:0">Signup for Newsletter:</h3>
      <div class="email-field">Enter Email...<b>Go</b></div>
    </div>
  </div>
  <span class="divider" style="left:738px"></span>
  <div class="col tweets">
    <h3><i></i>Latest Tweets:</h3>
    <div class="tweet">Lorem Ipsum is simply dummy text of the printing and typesetting industry.</div>
    <div class="tweet">Lorem Ipsum is simply dummy text of the printing and typesetting industry.</div>
    <div class="tweet" style="border:none">Lorem Ipsum is simply dummy text of the printing and typesetting industry.</div>
  </div>
  <span class="view-all" style="left:938px;top:137px">+ View All</span>
</footer>

<div class="abs bottom-bar">
  <div class="copyright">© Copyright Marlow Fenwick Studio | All Rights Reserved</div>
  <div class="footer-nav">Home &nbsp;|&nbsp; About Us &nbsp;|&nbsp; Contact Us</div>
</div>
</body>
</html>
```